Profesional personal website needs design and business card

I need a business card with my professional name as a logo "Marlo Vitality" for my business. I am a Wellness Coach, consultant and trainer. So it should be professional, wellness oriented and modern.

Target Market(s)

Private clients, governments, corporations. Luxury and high market.

Industry/Entity Type

Health And Wellness

Contact Information for Business Card

Marlo Vitality should be the logo

Colors

Designer to choose colors to be used in the design.

Requirements
Must have
• Marlo Vitality
• Name: Tomás Arribal
• Wellness Coach, Consultant & Trainer.
• Website: www.marlovitality.example
• Phone:
• Spain (+34) 612 480 397
• (USA) +1 (555) 318 2046
Nice to have
• The most important is the design of "Marlo Vitality", as this is going to be my personal brand logo. It should be professional, wellness, high end and actual.
Should not have
• no golds, no baroque style..

```html
<!DOCTYPE html>
<html lang="en">
<head>
<meta charset="utf-8">
<title>Marlo Vitality — Business Card</title>
<link rel="stylesheet" href="https://fonts.googleapis.com/css2?family=Open+Sans:wght@400;600;700&display=swap">
<style>
  :root {
    --slate: #44525b;
    --slate-deep: #3b474f;
    --teal: #6bb59e;
    --teal-light: #77bfa8;
    --paper: #eef0ef;
    --white: #ffffff;
    --card-w: 340px;
    --card-h: 595px;
  }
  * { box-sizing: border-box; margin: 0; padding: 0; }
  html, body {
    width: 1200px; height: 1200px; overflow: hidden;
    background: var(--paper);
    font-family: "Open Sans", Arial, sans-serif;
  }
  .sheet { position: relative; width: 1200px; height: 1200px; }

  .card {
    position: absolute; top: 280px;
    width: var(--card-w); height: var(--card-h);
    overflow: hidden;
    box-shadow: 0 10px 30px rgba(0,0,0,0.18);
  }
  .card__arc { position: absolute; inset: 0; width: 100%; height: 100%; }

  /* Front */
  .card--front { left: 215px; background: var(--teal); }
  .card--front .top-band {
    position: absolute; top: 0; left: 20px; right: 20px; height: 12px;
    background: var(--slate);
  }
  .brand {
    position: absolute; left: 0; right: 0; text-align: center;
    font-weight: 700; text-transform: uppercase; line-height: 1.05;
  }
  .card--front .brand {
    top: 232px; color: var(--slate);
    font-size: 50px; letter-spacing: 2px;
  }
  .brand__line { display: block; }
  .website {
    position: absolute; bottom: 14px; left: 0; right: 0; text-align: center;
    color: var(--slate); font-weight: 600; font-size: 14px; letter-spacing: 1.5px;
  }

  /* Back */
  .card--back { left: 645px; background: var(--slate); }
  .card--back .brand {
    top: 48px; color: var(--teal);
    font-size: 44px; letter-spacing: 2px;
  }
  .contact { position: absolute; left: 34px; right: 20px; top: 440px; color: var(--white); }
  .contact__name { font-weight: 700; font-size: 24px; line-height: 1.2; }
  .contact__role { font-size: 13px; margin-top: 2px; }
  .contact__phones { display: flex; align-items: center; gap: 12px; margin-top: 16px; }
  .phone-icon {
    width: 40px; height: 40px; background: var(--teal);
    display: flex; align-items: center; justify-content: center; flex: none;
  }
  .phone-list { font-size: 13px; line-height: 1.4; }
  .card--back .bottom-band {
    position: absolute; bottom: 0; left: 20px; right: 20px; height: 10px;
    background: var(--teal);
  }

  .swatches { position: absolute; right: 38px; bottom: 38px; display: flex; gap: 28px; }
  .swatch { width: 44px; height: 44px; border-radius: 50%; }
  .swatch--slate { background: var(--slate); }
  .swatch--teal { background: var(--teal); }
</style>
</head>
<body>
<main class="sheet">
  <section class="card card--front" aria-label="Card front">
    <svg class="card__arc" viewBox="0 0 340 595" aria-hidden="true">
      <circle cx="170" cy="720" r="520" fill="#000" fill-opacity="0.035"/>
    </svg>
    <div class="top-band"></div>
    <h1 class="brand"><span class="brand__line">Marlo</span><span class="brand__line">Vitality</span></h1>
    <p class="website">www.marlovitality.example</p>
  </section>

  <section class="card card--back" aria-label="Card back">
    <svg class="card__arc" viewBox="0 0 340 595" aria-hidden="true">
      <circle cx="170" cy="-60" r="480" fill="#fff" fill-opacity="0.03"/>
    </svg>
    <h2 class="brand"><span class="brand__line">Marlo</span><span class="brand__line">Vitality</span></h2>
    <div class="contact">
      <p class="contact__name">Tomás Arribal</p>
      <p class="contact__role">Wellness Coach, Consultant &amp; Trainer</p>
      <div class="contact__phones">
        <span class="phone-icon">
          <svg width="24" height="24" viewBox="0 0 24 24" aria-hidden="true">
            <path fill="#44525b" d="M6.6 10.8a15.1 15.1 0 0 0 6.6 6.6l2.2-2.2a1 1 0 0 1 1-.25 11.4 11.4 0 0 0 3.6.57 1 1 0 0 1 1 1V20a1 1 0 0 1-1 1A17 17 0 0 1 3 4a1 1 0 0 1 1-1h3.5a1 1 0 0 1 1 1c0 1.25.2 2.46.57 3.6a1 1 0 0 1-.25 1z"/>
          </svg>
        </span>
        <p class="phone-list">Spain (+34) 612 480 397<br>(USA) +1 (555) 318 2046</p>
      </div>
    </div>
    <div class="bottom-band"></div>
  </section>

  <div class="swatches" aria-label="Colour palette">
    <span class="swatch swatch--slate"></span>
    <span class="swatch swatch--teal"></span>
  </div>
</main>
</body>
</html>
```